I need cover art for my first album

I am releasing my first album and I need cover art for the CD  packaging. The art would also be used in Tunevault and other streaming services. The music is dark, experimental electronic music. It includes lots of soundscapes with industrial, metallic sounds. Similar artists include Grimvaar and Telo Vasquin. The album's concept is inspired by the loneliness and inherent dangers of long-term space travel and living alone in cold, distant space stations.
You can hear a rough cut of one of the tracks for the album at https://wavebarn.example/kolventra/outpost.

Colors
Designer to choose colors to be used in the design.
Requirements
Must have
- The design should be abstract and minimalist but not only grayscale. I would like to see color used in ways that convey feelings. Provide a sense of movement.
Should not have
- No images of moons or planets. Please don't be literal with the "space" theme.

```html
<!DOCTYPE html>
<html lang="en">
<head>
<meta charset="utf-8">
<title>Sunken Into Halosphere — Kolventra</title>
<link rel="stylesheet" href="https://fonts.googleapis.com/css2?family=Cinzel:wght@400&family=Oswald:wght@700&display=swap">
<style>
  :root {
    --void: #06020c;
    --violet-deep: #3a1477;
    --violet: #7d3fe0;
    --lavender: #b79af0;
    --haze: #e4dcfb;
    --glow: #ffffff;
    --ink: #0b0910;
  }
  * { margin: 0; padding: 0; box-sizing: border-box; }
  html, body {
    width: 1200px;
    height: 1197px;
    overflow: hidden;
    background: var(--void);
  }
  .cover {
    position: relative;
    width: 1200px;
    height: 1197px;
    overflow: hidden;
  }
  .cover-artwork {
    position: absolute;
    inset: 0;
    background:
      radial-gradient(ellipse 14% 14% at 55% 30%, rgba(25,6,50,0.9), transparent 75%),
      radial-gradient(ellipse 30% 24% at 20% 28%, rgba(200,170,250,0.8), transparent 72%),
      radial-gradient(ellipse 45% 30% at 75% 95%, var(--glow), transparent 70%),
      radial-gradient(ellipse 40% 25% at 70% 60%, var(--haze), transparent 70%),
      radial-gradient(ellipse 45% 40% at 30% 60%, var(--lavender), transparent 75%),
      radial-gradient(ellipse 45% 40% at 95% 20%, var(--void), transparent 80%),
      linear-gradient(170deg, var(--void) 0%, var(--violet-deep) 14%, var(--violet) 40%, var(--lavender) 72%, var(--haze) 100%);
  }
  .light-streaks {
    position: absolute;
    inset: 0;
    width: 1200px;
    height: 1197px;
  }
  .light-streaks line {
    stroke: var(--glow);
    stroke-linecap: round;
    opacity: 0.92;
  }
  .title {
    position: absolute;
    right: 92px;
    top: 812px;
    font-family: "Cinzel", "Trajan Pro", serif;
    font-weight: 400;
    font-size: 76px;
    line-height: 112px;
    letter-spacing: 7px;
    color: var(--ink);
    text-align: right;
    text-transform: uppercase;
    white-space: nowrap;
  }
  .title-line { display: block; }
  .artist {
    position: absolute;
    left: 1114px;
    top: 830px;
    writing-mode: vertical-rl;
    font-family: "Oswald", "Arial Narrow", sans-serif;
    font-weight: 700;
    font-size: 48px;
    line-height: 1;
    letter-spacing: 2px;
    color: var(--ink);
    text-transform: uppercase;
    white-space: nowrap;
  }
</style>
</head>
<body>
  <main class="cover">
    <div class="cover-artwork" role="img" aria-label="Abstract close-up of a pale, rippled organic surface lit in deep violet and lavender light, fading to black at the top"></div>

    <svg class="light-streaks" viewBox="0 0 1200 1197" aria-hidden="true">
      <line x1="845" y1="614" x2="1215" y2="310" stroke-width="14"/>
      <line x1="460" y1="900" x2="1215" y2="640" stroke-width="9"/>
      <line x1="0" y1="1195" x2="830" y2="735" stroke-width="18"/>
      <line x1="20" y1="1150" x2="250" y2="1030" stroke-width="16"/>
    </svg>

    <h1 class="title">
      <span class="title-line">Sunken Into</span>
      <span class="title-line">Halosphere</span>
    </h1>
    <p class="artist">Kolventra</p>
  </main>
</body>
</html>
```